marketing card

I need a fun and striking Marketing card to introduce our new office to attract new patients
our website is smilepathwaykids@mailbrook.net for more ideas
add coupon for $25.00 off your next filling
add coupon for free teeth whitening
make the card 9x6 size ,
The card downloaded I like rediscover your smile
free teeth whitening after exam,x-rays & cleaning
Target Market(s)
population in our area , anyone looking for a dental office
Industry/Entity Type
Health Care
Font styles to use
Serif
Colors
33a6d7
9bcb3c
Requirements
Must have
- Coupon for $25 off if you need a filling
- free whitening after teeth cleaning, x-rays & exam
- Our hygienist will come to you if you are home bound or in a nursing home facility
Nice to have
- want to be inviting and non intimating, we see all ages

```html
<!DOCTYPE html>
<html lang="en">
<head>
<meta charset="utf-8">
<title>Smile Pathway – New Patient Mailer</title>
<link rel="stylesheet" href="https://fonts.googleapis.com/css2?family=Lato:wght@300;400&family=Open+Sans:wght@400;600;700&display=swap">
<style>
:root{
  --sky:#33a6d7;
  --ocean:#1a6a9c;
  --lime:#8dbd35;
  --lime-light:#9bcb3c;
  --navy:#1d3e7c;
  --ink:#333;
  --grey:#555;
  --paper:#ffffff;
  --backdrop:#eef0f2;
}
*{margin:0;padding:0;box-sizing:border-box}
html,body{width:1057px;height:1200px;overflow:hidden;background:var(--backdrop)}
.stage{position:absolute;left:0;top:0;width:1300px;height:1476px;transform:scale(0.8131);transform-origin:0 0}
.card{position:absolute;left:175px;width:900px;height:600px;background:var(--paper);overflow:hidden;font-family:"Open Sans",sans-serif;box-shadow:0 2px 6px rgba(0,0,0,.18)}
.card-front{top:132px}
.card-back{top:792px}
.card svg.shapes{position:absolute;left:0;top:0;width:900px;height:600px}
.abs{position:absolute}
.headline{font-family:"Lato",sans-serif;font-weight:300;color:var(--paper);line-height:1}
.headline-main{font-size:72px}
.headline-sub{font-size:42px}
.tagline{width:420px;text-align:center;top:160px;color:var(--paper);font-family:"Lato",sans-serif;font-weight:300;font-size:17px;line-height:24px}
.coupon{top:230px;width:189px;height:143px;border-radius:8px;overflow:hidden;background:var(--lime-light);text-align:center;color:var(--paper)}
.coupon-label{height:34px;background:var(--paper);color:var(--ink);font-size:12px;font-weight:600;line-height:36px;border-radius:8px 8px 0 0}
.coupon-value{font-family:"Lato",sans-serif;font-size:54px;line-height:1;margin-top:8px}
.coupon-value sup{font-size:22px;vertical-align:top;position:relative;top:4px}
.coupon-value small{font-size:26px}
.coupon-detail{font-family:"Lato",sans-serif;font-size:18px;margin-top:6px}
.fine-print{left:0;width:430px;top:384px;text-align:center;color:var(--paper);font-family:"Lato",sans-serif;font-weight:300;font-size:17px;line-height:22px}
.fine-print .homebound{font-size:14px;font-weight:400}
.brand{color:var(--navy);font-family:"Open Sans",sans-serif;font-weight:700;line-height:1;letter-spacing:1px;display:flex;align-items:center;gap:12px;white-space:nowrap}
.brand-front{font-size:42px}
.brand-back{font-size:32px}
.brand-dot{width:20px;height:20px;border-radius:50%;background:var(--navy)}
.badge{left:438px;top:403px;width:124px;height:124px;border-radius:50%;background:var(--navy);border:3px solid var(--lime-light);box-shadow:0 0 0 4px var(--ocean);color:var(--paper);font-size:14px;line-height:19px;text-align:center;display:flex;align-items:center;justify-content:center}
.contact-front{left:595px;width:300px;top:512px;text-align:center;color:var(--paper)}
.phone{font-size:27px;line-height:1;display:flex;align-items:center;justify-content:center;gap:10px}
.phone svg{width:22px;height:22px}
.email{font-size:17px;margin-top:12px;white-space:nowrap}
.back-info{left:25px;width:360px;top:150px;text-align:center;color:var(--ink)}
.back-info .phone{color:var(--navy)}
.back-info .email{color:var(--navy);margin-top:8px}
.note{font-size:15px;line-height:19px;margin-top:16px}
.web{color:var(--navy);font-size:18px;margin-top:12px}
.social{display:flex;justify-content:center;gap:4px;margin-top:10px}
.social span{width:26px;height:26px;border-radius:3px;background:var(--navy)}
.return-address{left:509px;top:33px;color:var(--grey);font-size:15px;line-height:19.5px;font-style:normal}
.return-address .name{font-size:14px;margin-bottom:10px}
.postage{left:770px;top:27px;width:97px;height:96px;border:1px solid #777;font-family:Arial,sans-serif;font-size:12.5px;line-height:15.6px;text-align:center;color:#111;padding-top:7px}
.postage b{font-weight:700}
</style>
</head>
<body>
<div class="stage">

  <section class="card card-front">
    <svg class="shapes" viewBox="0 0 900 600">
      <defs>
        <linearGradient id="frontSky" x1="0" y1="0" x2="1" y2="0">
          <stop offset="0" stop-color="#33a6d7"/>
          <stop offset="1" stop-color="#1a6a9c"/>
        </linearGradient>
        <linearGradient id="photoTone" x1="0" y1="0" x2="1" y2="1">
          <stop offset="0" stop-color="#7e8790"/>
          <stop offset="0.5" stop-color="#b9c6cf"/>
          <stop offset="1" stop-color="#d8cf8e"/>
        </linearGradient>
        <linearGradient id="panelBlue" x1="0" y1="0" x2="1" y2="0">
          <stop offset="0" stop-color="#1d6ea3"/>
          <stop offset="1" stop-color="#175f8e"/>
        </linearGradient>
      </defs>
      <rect width="900" height="600" fill="url(#frontSky)"/>
      <path role="img" aria-label="Photo of a laughing young couple holding a red ribbon" d="M598 0 H900 V478 H470 C430 360 460 150 598 0 Z" fill="url(#photoTone)"/>
      <path d="M590 0 C440 140 405 400 610 600" fill="none" stroke="#8dbd35" stroke-width="10"/>
      <path d="M0 447 C220 432 430 440 560 560 L600 600 H0 Z" fill="#ffffff"/>
      <path d="M0 440 C220 425 430 432 560 552 L612 600" fill="none" stroke="#8dbd35" stroke-width="10"/>
      <path d="M900 488 V600 H640 C600 565 560 525 520 488 Z" fill="url(#panelBlue)"/>
      <path d="M520 482 H900" stroke="#8dbd35" stroke-width="10"/>
      <path d="M530 494 H900" stroke="#ffffff" stroke-width="4"/>
    </svg>

    <h1 class="headline headline-main abs" style="left:20px;top:22px">Rediscover</h1>
    <p class="headline headline-sub abs" style="left:214px;top:96px">Your Smile!</p>
    <p class="tagline abs" style="left:-5px">You Will Stand Taller, Laugh Longer &amp; Smile More.<br>A Smile Can Change Your Life!</p>

    <div class="coupon abs" style="left:13px">
      <div class="coupon-label">NEW PATIENT SPECIAL</div>
      <div class="coupon-value"><sup>$</sup>25<small>off</small></div>
      <div class="coupon-detail">YOUR NEXT FILLING</div>
    </div>
    <div class="coupon abs" style="left:228px">
      <div class="coupon-label">NEW PATIENT SPECIAL</div>
      <div class="coupon-value">FREE</div>
      <div class="coupon-detail">TEETH WHITENING</div>
    </div>
    <p class="fine-print abs">Free teeth whitening after exam, x-rays &amp; cleaning.<br><span class="homebound">Home bound or in a nursing home? Our hygienist will come to you!</span></p>

    <div class="brand brand-front abs" style="left:32px;top:502px"><span class="brand-dot"></span>SMILE PATHWAY</div>

    <div class="badge abs"><span>SCHEDULE AN<br>APPOINTMENT<br>TODAY</span></div>

    <div class="contact-front abs">
      <div class="phone"><svg viewBox="0 0 24 24"><path fill="#ffffff" d="M6.6 10.8a15.1 15.1 0 0 0 6.6 6.6l2.2-2.2a1 1 0 0 1 1-.25 11.4 11.4 0 0 0 3.6.57 1 1 0 0 1 1 1V20a1 1 0 0 1-1 1A17 17 0 0 1 3 4a1 1 0 0 1 1-1h3.5a1 1 0 0 1 1 1c0 1.25.2 2.45.57 3.57a1 1 0 0 1-.25 1z"/></svg>385-555-0184</div>
      <div class="email">smilepathwaykids@mailbrook.net</div>
    </div>
  </section>

  <section class="card card-back">
    <svg class="shapes" viewBox="0 0 900 600">
      <defs>
        <linearGradient id="bandBlue" x1="0" y1="0" x2="1" y2="0">
          <stop offset="0" stop-color="#33a6d7"/>
          <stop offset="1" stop-color="#1a5f8e"/>
        </linearGradient>
        <linearGradient id="mapTone" x1="0" y1="0" x2="1" y2="1">
          <stop offset="0" stop-color="#eeeeee"/>
          <stop offset="1" stop-color="#e6d9c4"/>
        </linearGradient>
      </defs>
      <path d="M348 0 C430 110 478 230 486 330" fill="none" stroke="#8dbd35" stroke-width="12"/>
      <path d="M388 0 C452 110 488 230 492 330" fill="none" stroke="#1f7fb6" stroke-width="10"/>
      <path d="M0 482 H420 C620 482 800 530 900 598 V600 H0 Z" fill="url(#bandBlue)"/>
      <path d="M0 478 H420 C620 478 800 526 900 594" fill="none" stroke="#8dbd35" stroke-width="8"/>
      <circle cx="472" cy="406" r="100" fill="#ffffff"/>
      <circle role="img" aria-label="Street map showing the office location" cx="472" cy="406" r="92" fill="url(#mapTone)"/>
      <path d="M560 237 H866 M560 278 H866 M560 319 H866 M560 360 H866" stroke="#b8bcc2" stroke-width="1.2"/>
    </svg>

    <div class="brand brand-back abs" style="left:40px;top:62px"><span class="brand-dot"></span>SMILE PATHWAY</div>

    <div class="back-info abs">
      <div class="phone"><svg viewBox="0 0 24 24"><path fill="#1d3e7c" d="M6.6 10.8a15.1 15.1 0 0 0 6.6 6.6l2.2-2.2a1 1 0 0 1 1-.25 11.4 11.4 0 0 0 3.6.57 1 1 0 0 1 1 1V20a1 1 0 0 1-1 1A17 17 0 0 1 3 4a1 1 0 0 1 1-1h3.5a1 1 0 0 1 1 1c0 1.25.2 2.45.57 3.57a1 1 0 0 1-.25 1z"/></svg>385-555-0184</div>
      <div class="email">smilepathwaykids@mailbrook.net</div>
      <p class="note">Some procedures require a specialty Dentist for futher treatment or investigation.<br>If you have questions about a possible refferal come see us for a free Second Opinion.</p>
      <p class="note">Our purpose is to make sure you get to see the right specialist for your needs, at the right time and in the right place.</p>
      <div class="web">www.smilepathwaykids.com</div>
      <div class="social"><span></span><span></span><span></span></div>
    </div>

    <address class="return-address abs">
      <div class="name">SMILE PATHWAY</div>
      2150 W. 9800 S. #110<br>
      Lindon Falls, UT 84000<br>
      (Northwest corner of Maple Grill)
    </address>

    <div class="postage abs">PRSRT STD<br>ECRWSS<br>U.S. POSTAGE<br><b>PAID</b><br>EDDM RETAIL</div>

    <p class="headline headline-main abs" style="left:35px;top:500px">Rediscover</p>
    <p class="headline headline-sub abs" style="left:385px;top:524px">Your Smile!</p>
  </section>

</div>
</body>
</html>
```